Online Consultancy Needs a New Logo & Business Card Design

Based on the new logo we just received from another contest here on Maketrove,

You'll find a few different versions of our logo as well as examples of business card designs we like in this folder:
==> https://share.plumvault.net/folderview?id=7Kq2WzTn4pLrXcv9BsHaYe1MoD5g&usp=sharing

We are considering two options:
- clean, black design
- clean, white/blue design

We're willing to consider both options.

We're considering adding some special effects to the cards when printing - emboss, rounded corners, etc.

However, please deliver a design WITHOUT round corners.

Target Market(s)

Successful business people, serious and older audience.

Industry/Entity Type

Business

Contact Information for Business Card

For the business card, I would like a minimalistic card with the logo on one side (perhaps in the middle) and the contact information on the other.

For the contact information please use:
Name: Peter Lund
Position: Founder
Email: peter.lund@korvim.com
Phone Number: +381 63 98 76 210
Website URL: www.korvim.com

Font styles to use
Serif
Sans Serif

Requirements
Must have
• Must fit in perfectly with our current website design.

```html
<!DOCTYPE html>
<html lang="en">
<head>
<meta charset="utf-8">
<title>Korvim – Business Card</title>
<link href="https://fonts.googleapis.com/css2?family=Quantico:wght@400;700&display=swap" rel="stylesheet">
<style>
  :root {
    --page-bg: #8a8a8a;
    --card-dark: #333333;
    --card-light-top: #f4f4f4;
    --card-light-bottom: #d9d9d9;
    --pill-top: #e6e6e6;
    --pill-bottom: #c9c9c9;
    --pill-edge: #b5b5b5;
    --ink: #2b2b2b;
    --white: #ffffff;
    --divider: #c4c4c4;
  }
  * { box-sizing: border-box; margin: 0; padding: 0; }
  html, body { width: 1200px; height: 1200px; overflow: hidden; }
  body {
    background: var(--page-bg);
    font-family: "Quantico", sans-serif;
    display: flex;
    align-items: center;
    justify-content: center;
    gap: 70px;
  }
  .card {
    width: 420px;
    height: 735px;
    background: linear-gradient(180deg, var(--card-light-top), var(--card-light-bottom));
    display: flex;
    flex-direction: column;
    box-shadow: 0 10px 30px rgba(0,0,0,0.25);
  }
  .card-header {
    background: var(--card-dark);
    color: var(--white);
    height: 300px;
    display: flex;
    flex-direction: column;
    align-items: center;
    justify-content: center;
    gap: 22px;
  }
  .brand {
    display: flex;
    align-items: center;
    gap: 16px;
    font-size: 64px;
    font-weight: 700;
    letter-spacing: 1px;
    color: var(--white);
  }
  .brand-dot {
    width: 34px;
    height: 34px;
    border-radius: 50%;
    background: var(--white);
  }
  .person { text-align: center; line-height: 1.25; }
  .person-name { font-size: 20px; letter-spacing: 2px; text-transform: uppercase; }
  .person-role { font-size: 14px; letter-spacing: 2px; text-transform: uppercase; }
  .contact-list {
    list-style: none;
    flex: 1;
    display: flex;
    flex-direction: column;
    justify-content: space-evenly;
    padding: 10px 0;
  }
  .contact-row {
    padding: 0 28px 26px;
    border-bottom: 1px solid var(--divider);
  }
  .contact-row:last-child { border-bottom: none; padding-bottom: 0; }
  .contact-pill {
    display: flex;
    align-items: center;
    gap: 12px;
    height: 44px;
    padding: 0 12px 0 8px;
    border-radius: 8px;
    background: linear-gradient(180deg, var(--pill-top), var(--pill-bottom));
    border: 1px solid var(--pill-edge);
    color: var(--ink);
    font-size: 19px;
    white-space: nowrap;
  }
  .contact-pill.tall { height: 64px; font-size: 16px; white-space: normal; line-height: 1.2; }
  .contact-icon {
    flex: 0 0 30px;
    width: 30px;
    height: 30px;
    border-radius: 5px;
    background: var(--card-light-top);
    border: 1px solid var(--pill-edge);
    display: flex;
    align-items: center;
    justify-content: center;
  }
  .contact-icon svg { width: 18px; height: 18px; fill: none; stroke: var(--ink); stroke-width: 1.8; }
  .social-mark { width: 14px; height: 14px; background: var(--ink); border-radius: 2px; }
</style>
</head>
<body>

  <section class="card card-back">
    <header class="card-header">
      <div class="brand"><span class="brand-dot"></span>korvim</div>
    </header>
    <ul class="contact-list">
      <li class="contact-row"><div class="contact-pill"><span class="contact-icon"><span class="social-mark"></span></span>chatterly.net/korvim</div></li>
      <li class="contact-row"><div class="contact-pill"><span class="contact-icon"><span class="social-mark"></span></span>tweetline.net/korvim</div></li>
      <li class="contact-row"><div class="contact-pill"><span class="contact-icon"><span class="social-mark"></span></span>proflink.net/korvim</div></li>
    </ul>
  </section>

  <section class="card card-front">
    <header class="card-header">
      <div class="brand"><span class="brand-dot"></span>korvim</div>
      <div class="person">
        <p class="person-name">Peter Lund</p>
        <p class="person-role">General Manager</p>
      </div>
    </header>
    <ul class="contact-list">
      <li class="contact-row"><div class="contact-pill">
        <span class="contact-icon"><svg viewBox="0 0 24 24"><path d="M5 3h4l2 5-3 2a12 12 0 0 0 6 6l2-3 5 2v4a2 2 0 0 1-2 2A18 18 0 0 1 3 5a2 2 0 0 1 2-2z"/></svg></span>
        +381 63 98 76 210</div></li>
      <li class="contact-row"><div class="contact-pill">
        <span class="contact-icon"><svg viewBox="0 0 24 24"><rect x="3" y="5" width="18" height="14" rx="1"/><path d="M3 6l9 7 9-7"/></svg></span>
        peter.lund@korvim.com</div></li>
      <li class="contact-row"><div class="contact-pill">
        <span class="contact-icon"><svg viewBox="0 0 24 24"><circle cx="12" cy="12" r="9"/><path d="M3 12h18M12 3c3 3 3 15 0 18M12 3c-3 3-3 15 0 18"/></svg></span>
        www.korvim.com</div></li>
      <li class="contact-row"><div class="contact-pill tall">
        <span class="contact-icon"><svg viewBox="0 0 24 24"><path d="M12 22s7-7 7-12a7 7 0 0 0-14 0c0 5 7 12 7 12z"/><circle cx="12" cy="10" r="2.5"/></svg></span>
        42 Harbour Lane, Unit 7<br>Northgate Ave.</div></li>
    </ul>
  </section>

</body>
</html>
```